Construction Company Needs Letterhead Design

We recently had a new logo designed and would like to have our letterhead updated to a trendier design. We are a concrete construction company based out of Iowa, but do work for Agricultural businesses across the Midwest.

Industry/Entity Type

Construction

Colors
ec1f27
000000
ffffff

Requirements
Must have
• Must stay within our current color scheme of red/black/white. Must have have our address, phone number, e-mail address, etc. printed on the letterhead as well.

```html
<!DOCTYPE html>
<html lang="en">
<head>
<meta charset="utf-8">
<title>Brenhold Letterhead</title>
<link href="https://fonts.googleapis.com/css2?family=Lato:wght@400;700;900&display=swap" rel="stylesheet">
<style>
  :root {
    --brand-red: #ec1f27;
    --brand-black: #1a1a1a;
    --paper: #ffffff;
    --backdrop: #d2d3d5;
    --body-text: #6b6b6b;
    --heading-text: #333333;
  }
  * { margin: 0; padding: 0; box-sizing: border-box; }
  html, body { width: 1200px; height: 1200px; overflow: hidden; background: var(--backdrop); }
  body { font-family: "Lato", sans-serif; position: relative; }
  .letterhead {
    position: absolute; left: 196px; top: 29px;
    width: 808px; height: 1142px; background: var(--paper);
  }
  .side-band { position: absolute; left: 69px; width: 38px; }
  .side-band--red { top: 0; height: 60px; background: var(--brand-red); }
  .side-band--black { top: 140px; bottom: 0; background: var(--brand-black); }
  .brand-mark {
    position: absolute; left: 67px; top: 80px; width: 42px; height: 42px;
    background: var(--brand-black);
  }
  .brand-name {
    position: absolute; left: 120px; top: 72px;
    font-weight: 900; font-size: 36px; letter-spacing: 1px;
    color: var(--brand-black); line-height: 1;
  }
  .recipient { position: absolute; left: 158px; top: 186px; color: var(--heading-text); }
  .recipient__salutation { font-weight: 700; font-size: 14px; }
  .recipient__line { display: inline-block; width: 78px; border-bottom: 1px solid var(--heading-text); }
  .recipient__role { font-size: 9.5px; margin-top: 1px; }
  .recipient__company { font-size: 9.5px; font-weight: 700; margin-top: 3px; }
  .letter-date {
    position: absolute; right: 70px; top: 190px;
    font-size: 10px; font-weight: 700; color: var(--heading-text);
  }
  .letter-body {
    position: absolute; left: 158px; top: 267px; width: 582px;
    font-size: 13.2px; line-height: 16.3px; color: var(--body-text);
    text-align: justify;
  }
  .letter-body p { margin-bottom: 18px; }
  .letter-body p.lead { font-weight: 700; color: #555; margin-bottom: 17px; }
  .signature {
    position: absolute; left: 160px; top: 805px; width: 120px; height: 36px;
    background: linear-gradient(180deg, #f4f4f4, #e6e6e6);
    border-bottom: 1px solid #444;
  }
  .signer { position: absolute; left: 161px; top: 858px; }
  .signer__name { color: var(--brand-red); font-weight: 900; font-size: 16.5px; letter-spacing: 0.5px; }
  .signer__role { font-size: 12.5px; color: var(--heading-text); margin-top: 2px; }
  .contact-list { position: absolute; left: 128px; top: 955px; list-style: none; }
  .contact-list li {
    display: flex; align-items: center; height: 26.5px;
    font-size: 9.5px; color: var(--heading-text);
  }
  .contact-list svg { width: 16px; height: 16px; margin-right: 18px; fill: var(--brand-red); }
</style>
</head>
<body>
  <main class="letterhead">
    <div class="side-band side-band--red"></div>
    <div class="side-band side-band--black"></div>
    <div class="brand-mark"></div>
    <div class="brand-name">BRENHOLD</div>

    <div class="recipient">
      <div class="recipient__salutation">Dear, Mr<span class="recipient__line"></span></div>
      <div class="recipient__role">Designation</div>
      <div class="recipient__company">COMPANY NAME</div>
    </div>
    <div class="letter-date">DATE:08/02/2018</div>

    <section class="letter-body">
      <p>Lorem Ipsum is simply dummy text of the printing and typesetting industry. Lorem Ipsum has been the industry's standard dummy text ever since the 1500s,when an unknown printer took a galley of type and scrambled it to make a type specimen book. It has survived not only five centuries, but also the leap into electronic typesetting, remaining essentially unchanged. It was popularised in the 1960s with the release of Letraset sheets containing Lorem Ipsum passages,and more recently with desktop publishing software like Aldus PageMaker including versions of Lorem Ipsum.</p>
      <p class="lead">Lorem Ipsum is simply dummy text of the printing and typesetting industry. Lorem Ipsum has been the industry's standard dummy text ever since the 1500s,when an unknown printer took a galley of type and scrambled it to make a type specimen book.</p>
      <p>Lorem Ipsum is simply dummy text of the printing and typesetting industry. Lorem Ipsum has been the industry's standard dummy text ever since the 1500s,when an unknown printer took a galley of type and scrambled it to make a type specimen book. It has survived not only five centuries, but also the leap into electronic typesetting, remaining essentially unchanged. It was popularised in the 1960s with the release of Letraset sheets containing Lorem Ipsum passages,and more recently with desktop publishing software like Aldus PageMaker including versions of Lorem Ipsum.It was popularised in the 1960s with the release of Letraset sheets containing Lorem Ipsum passages,and more recently with desktop publishing software like Aldus PageMaker including versions of Lorem Ipsum.</p>
      <p>Lorem Ipsum is simply dummy text of the printing and typesetting industry. Lorem Ipsum has been the industry's standard dummy text ever since the 1500s,when an unknown printer took a galley of type and scrambled it to make a type specimen book. It has survived not only five centuries, but also the leap into electronic typesetting, remaining essentially unchanged. It was popularised in the 1960s with the release of Letraset sheets containing Lorem Ipsum passages,and more recently with desktop publishing software like Aldus PageMaker including versions of Lorem Ipsum.</p>
    </section>

    <div class="signature" role="img" aria-label="Handwritten signature"></div>
    <div class="signer">
      <div class="signer__name">YOUR NAME</div>
      <div class="signer__role">Designation</div>
    </div>

    <ul class="contact-list">
      <li><svg viewBox="0 0 24 24" aria-hidden="true"><path d="M6.6 10.8a15 15 0 0 0 6.6 6.6l2.2-2.2c.3-.3.7-.4 1-.2 1.1.4 2.3.6 3.6.6.6 0 1 .4 1 1V20c0 .6-.4 1-1 1A17 17 0 0 1 3 4c0-.6.4-1 1-1h3.5c.6 0 1 .4 1 1 0 1.3.2 2.5.6 3.6.1.3 0 .7-.2 1z"/></svg>+123-456-7899</li>
      <li><svg viewBox="0 0 24 24" aria-hidden="true"><path d="M6 2h12v5H6zM3 8h18a1 1 0 0 1 1 1v8h-4v5H6v-5H2V9a1 1 0 0 1 1-1zm5 7v5h8v-5z"/></svg>+123-456-7899</li>
      <li><svg viewBox="0 0 24 24" aria-hidden="true"><path d="M2 5h20v14H2zm2 2v.5l8 5.5 8-5.5V7l-8 5.5z"/></svg>info@brenhold.com</li>
      <li><svg viewBox="0 0 24 24" aria-hidden="true"><path d="M12 2a10 10 0 1 0 0 20 10 10 0 0 0 0-20zm0 2c.9 1 1.7 2.6 2 4h-4c.3-1.4 1.1-3 2-4zM4.3 10h3.8a14 14 0 0 0 0 4H4.3a8 8 0 0 1 0-4zm5.8 0h3.8a12 12 0 0 1 0 4h-3.8a12 12 0 0 1 0-4zm5.8 0h3.8a8 8 0 0 1 0 4h-3.8a14 14 0 0 0 0-4zM10 16h4c-.3 1.4-1.1 3-2 4-.9-1-1.7-2.6-2-4z"/></svg>www.brenhold.com</li>
      <li><svg viewBox="0 0 24 24" aria-hidden="true"><path d="M12 2a7 7 0 0 0-7 7c0 5 7 13 7 13s7-8 7-13a7 7 0 0 0-7-7zm0 9.5a2.5 2.5 0 1 1 0-5 2.5 2.5 0 0 1 0 5z"/></svg>27 Orchard Ln. Cedar Falls, IA 50613</li>
    </ul>
  </main>
</body>
</html>
```